Australian Software Consultancy needs new Business Card Design

Design Business Card based on existing design artefacts (attached). We are open to all designs. As its a 2 sided design and we thought it might be quite striking to have one side with a black background and te other side with a white background.

Target Market(s)

Financial Services mainly.

Industry/Entity Type

Business

Contact Information for Business Card

Name :
Position :
Email :

Requirements
Must have
• Funky design using our existing assets

```html
<!DOCTYPE html>
<html lang="en">
<head>
<meta charset="utf-8">
<title>Inner Orbit – Business Card</title>
<link href="https://fonts.googleapis.com/css2?family=Montserrat:wght@500;700&family=Lato:wght@400;700&display=swap" rel="stylesheet">
<style>
  :root {
    --bg: #8f8f8f;
    --black: #030303;
    --white: #ffffff;
    --red: #e8202a;
    --grey-text: #f2f2f2;
  }
  * { box-sizing: border-box; margin: 0; padding: 0; }
  html, body { width: 1200px; height: 945px; overflow: hidden; }
  body {
    background: var(--bg);
    position: relative;
    font-family: "Lato", Arial, sans-serif;
  }
  .card {
    position: absolute;
    left: 290px;
    width: 620px;
    height: 354px;
    border-radius: 22px;
    overflow: hidden;
  }

  /* Back side */
  .card--back { top: 70px; background: var(--red); }
  .card--back .back-panel {
    position: absolute; inset: 0 0 22px 0;
    background: var(--black);
    border-radius: 22px 22px 30px 30px;
  }
  .back-brand {
    position: absolute; left: 0; right: 0; top: 0; bottom: 22px;
    display: flex; align-items: center; justify-content: center; gap: 18px;
  }
  .back-brand .brand-ring {
    width: 58px; height: 58px; border-radius: 50%;
    border: 7px solid var(--red);
  }
  .back-brand .brand-name {
    font-family: "Montserrat", Arial, sans-serif;
    font-weight: 700; font-size: 40px; letter-spacing: 1px;
    color: var(--red);
  }

  /* Front side */
  .card--front { top: 500px; background: var(--white); }
  .front-dark {
    position: absolute; left: 0; right: 0; top: 0; height: 288px;
    background: var(--black);
  }
  .front-top-accent {
    position: absolute; left: 0; right: 0; top: 0; height: 172px;
    background: var(--red);
    border-radius: 0 0 30px 30px;
  }
  .front-top {
    position: absolute; left: 0; right: 0; top: 0; height: 168px;
    background: var(--white);
    border-radius: 0 0 30px 30px;
    display: flex; align-items: center; justify-content: center;
  }
  .wordmark {
    font-family: "Montserrat", Arial, sans-serif;
    font-weight: 700; font-size: 54px; letter-spacing: 2px;
    color: var(--black);
    margin-top: 26px;
  }
  .front-info {
    position: absolute; left: 0; right: 0; top: 190px;
    display: flex; align-items: center; justify-content: center;
  }
  .holder { text-align: right; padding-right: 26px; }
  .holder-name {
    font-family: "Lato", Arial, sans-serif;
    font-weight: 700; font-size: 25px; color: var(--red);
  }
  .holder-role {
    font-size: 15px; letter-spacing: 3px; color: var(--grey-text);
    margin-top: 4px;
  }
  .divider { width: 2px; height: 74px; background: var(--white); }
  .contacts { list-style: none; padding-left: 26px; }
  .contacts li {
    display: flex; align-items: center; gap: 12px;
    font-size: 15px; letter-spacing: 1px; color: var(--grey-text);
    line-height: 25px;
  }
  .contacts .icon {
    width: 15px; height: 15px; border-radius: 3px;
    background: var(--red);
    display: flex; align-items: center; justify-content: center;
  }
  .front-rule {
    position: absolute; left: 0; right: 0; top: 304px; height: 6px;
    background: var(--red);
  }
</style>
</head>
<body>

  <section class="card card--back" aria-label="Card back">
    <div class="back-panel"></div>
    <div class="back-brand">
      <span class="brand-ring"></span>
      <span class="brand-name">INNER ORBIT</span>
    </div>
  </section>

  <section class="card card--front" aria-label="Card front">
    <div class="front-dark"></div>
    <div class="front-top-accent"></div>
    <div class="front-top">
      <span class="wordmark">INNER ORBIT</span>
    </div>

    <div class="front-info">
      <div class="holder">
        <p class="holder-name">Daniel R. Hart</p>
        <p class="holder-role">FOUNDER / CEO</p>
      </div>
      <span class="divider"></span>
      <ul class="contacts">
        <li>
          <span class="icon">
            <svg width="9" height="9" viewBox="0 0 10 10"><path d="M2 1l2 2-1 1.3c.6 1.2 1.5 2.1 2.7 2.7L7 6l2 2-1.3 1.3C4.5 9 1 5.5.7 2.3z" fill="#fff"/></svg>
          </span>
          100.200.300
        </li>
        <li>
          <span class="icon">
            <svg width="9" height="9" viewBox="0 0 10 10"><rect x="0.5" y="2" width="9" height="6" fill="none" stroke="#fff" stroke-width="1.2"/><path d="M.5 2.5L5 6l4.5-3.5" fill="none" stroke="#fff" stroke-width="1.2"/></svg>
          </span>
          hello@inner-orbit.com
        </li>
        <li>
          <span class="icon">
            <svg width="9" height="9" viewBox="0 0 10 10"><circle cx="5" cy="5" r="4" fill="none" stroke="#fff" stroke-width="1.2"/><path d="M1 5h8M5 1c-2 2.5-2 5.5 0 8M5 1c2 2.5 2 5.5 0 8" fill="none" stroke="#fff" stroke-width="1"/></svg>
          </span>
          www.inner-orbit.com
        </li>
      </ul>
    </div>

    <div class="front-rule"></div>
  </section>

</body>
</html>
```